Letterhead design for Sleep Consulting Business

I'm looking for a new letterhead (heading/footer) design for my Sleep Consulting Business, I work with families to help their children improve their sleep.

The heading/footer will used in Microsoft Word Only-to be used for all of my documents such as writing Sleep Plans. I need to utilize as much working space in the document as possible. This will NOT be printed out on paper- it will only be used for heading/footer on microsoft word, then emailed to clients, who may print it at home.

My brand colors:
Dark Blue Hex: 1F2A42
Lighter Blueish Hex: 90BEC9
You're welcome to check out my website for inspiration- it is freshly created with other colors as well, and I love the outcome. www.hollowpinerest.com

Target Market(s)

Tired parents

Font styles to use
Script
Other font styles liked:
• Great Vibe, Lato or Just Another Hand are all used currently for my brand. Open to other options.

Requirements
Must have
• The letterhead (heading/footer) MUST be kept narrow (height-wise), so I have plenty of space on my document, while including important information.

It should look professional on screen, and when printed.

Must include my business name OR logo (Hollow Pine Sleep Consulting), and my email address. Mara@hollowpinerest.com

Website is optional, not required, just if you need to fill in a spot: www.hollowpinerest.com

```html
<!DOCTYPE html>
<html lang="en">
<head>
<meta charset="utf-8">
<title>Hollow Pine Sleep Consulting – Letterhead</title>
<link rel="stylesheet" href="https://fonts.googleapis.com/css2?family=Great+Vibes&family=Lato:wght@400&display=swap">
<style>
  :root {
    --brand-dark: #1F2A42;
    --brand-light: #90BEC9;
    --paper: #FFFFFF;
    --hang-tint: #F2F2F4;
    --rule: #3A4256;
  }
  * { margin: 0; padding: 0; box-sizing: border-box; }
  html, body {
    width: 938px;
    height: 1200px;
    overflow: hidden;
    background: var(--paper);
  }
  .letterhead {
    position: relative;
    width: 938px;
    height: 1200px;
    background: var(--paper);
    font-family: "Lato", sans-serif;
    color: var(--brand-dark);
  }
  .brand {
    position: absolute;
    left: 30px;
    top: 30px;
    display: flex;
    align-items: center;
    gap: 16px;
    z-index: 1;
  }
  .brand-dot {
    width: 88px;
    height: 88px;
    border-radius: 50%;
    background: var(--brand-light);
    flex: none;
  }
  .brand-name {
    font-family: "Great Vibes", cursive;
    font-size: 40px;
    font-weight: 400;
    line-height: 0.95;
    color: var(--brand-dark);
    white-space: nowrap;
  }
  .brand-name span { display: block; }
  .hanging-decor {
    position: absolute;
    left: 451px;
    top: 0;
    width: 458px;
    height: 428px;
    background: linear-gradient(180deg, rgba(242,242,244,0.35) 0%, rgba(242,242,244,0.7) 70%, rgba(255,255,255,0) 100%);
  }
  .footer-rule {
    position: absolute;
    top: 1162px;
    height: 1px;
    background: var(--rule);
  }
  .footer-rule.left { left: 0; width: 158px; }
  .footer-rule.right { left: 781px; width: 157px; }
  .contact-box {
    position: absolute;
    left: 158px;
    top: 1141px;
    width: 623px;
    height: 42px;
    border: 1px solid var(--rule);
    display: flex;
    align-items: center;
    justify-content: space-between;
    padding: 0 8px 0 8px;
  }
  .contact-item {
    display: flex;
    align-items: center;
    gap: 8px;
    font-family: "Great Vibes", cursive;
    font-size: 31px;
    line-height: 1;
    color: var(--brand-dark);
    white-space: nowrap;
  }
  .contact-icon { width: 17px; height: 17px; flex: none; }
</style>
</head>
<body>
  <main class="letterhead">
    <div class="hanging-decor" role="img" aria-label="Faint hanging stars on strings decorating the top right of the page"></div>

    <header class="brand">
      <span class="brand-dot"></span>
      <h1 class="brand-name"><span>Hollow Pine</span><span>Sleep Consulting</span></h1>
    </header>

    <footer>
      <span class="footer-rule left"></span>
      <div class="contact-box">
        <span class="contact-item">
          <svg class="contact-icon" viewBox="0 0 20 20" aria-hidden="true">
            <circle cx="10" cy="10" r="10" fill="var(--brand-light)"/>
            <rect x="5" y="6.5" width="10" height="7" fill="none" stroke="#fff" stroke-width="1.3"/>
            <path d="M5 6.5 L10 10.5 L15 6.5" fill="none" stroke="#fff" stroke-width="1.3"/>
          </svg>
          mara@hollowpinerest.com
        </span>
        <span class="contact-item">
          <svg class="contact-icon" viewBox="0 0 20 20" aria-hidden="true">
            <circle cx="10" cy="10" r="10" fill="var(--brand-light)"/>
            <circle cx="10" cy="10" r="5.5" fill="none" stroke="#fff" stroke-width="1"/>
            <ellipse cx="10" cy="10" rx="2.5" ry="5.5" fill="none" stroke="#fff" stroke-width="1"/>
            <path d="M4.5 10 H15.5 M5.3 7.3 H14.7 M5.3 12.7 H14.7" stroke="#fff" stroke-width="1"/>
          </svg>
          www.hollowpinerest.com
        </span>
      </div>
      <span class="footer-rule right"></span>
    </footer>
  </main>
</body>
</html>
```